Harborline Talent Web Site

I would like to change our current website to a better design. www.harborlinetalent.net.
Use the content from the this website.
Updates
The web site is down until 7AM EST on 3/25 for server maintenance. Sorry for the inconvenience.
REMEMBER: I am changing the website to focus on science and technical jobs across all industries. So, if your images focus on only biotech or only DNA or beakers that will not serve Aerospace very well or curcuit board manufacturing. So, either use a montage of images that cover everything or make you images more abstract.
Target Market(s)
We are now staffing for all science and technical jobs. Not just biotech and pharmaceutical.
So, pharmaceutical, biotech, aerospace, alternative energy, research, medical...etc. Anyone with a science or tehcnical background.
Number of Pages Required
5+ pages
Requirements
Must have
- Tag line: "The Science of Recruiting" replaces "A pharmaceutical and bitech search firm"
Pictures and images across more industries.
The job serach page only needs a banner. That page is being worked internally.

```html
<!DOCTYPE html>
<html lang="en">
<head>
<meta charset="utf-8">
<title>Harborline Talent — The Science of Recruiting</title>
<link href="https://fonts.googleapis.com/css2?family=Arimo:wght@400;700&display=swap" rel="stylesheet">
<style>
  :root {
    --green-dark: #0d3a1c;
    --green-text: #1d5a23;
    --orange: #c8720b;
    --ink: #333333;
    --ink-soft: #555555;
    --ink-muted: #777777;
    --panel-left: #dedede;
    --panel-right: #f1f1f1;
    --nav-idle: #e4e4e4;
    --rule: #e2e2e2;
    --page: #ffffff;
  }
  * { margin: 0; padding: 0; box-sizing: border-box; }
  html, body {
    width: 1200px; height: 960px; overflow: hidden;
    background: var(--page);
    font-family: "Arimo", Arial, sans-serif;
    color: var(--ink);
  }
  .canvas { position: relative; width: 1200px; height: 960px; }

  .backdrop {
    position: absolute; left: 70px; top: 0; width: 520px; height: 200px;
    background: linear-gradient(180deg, rgba(0,0,0,0.035), rgba(0,0,0,0.01));
  }
  .backdrop--lower {
    left: 70px; top: 610px; width: 420px; height: 220px;
    background: linear-gradient(180deg, rgba(0,0,0,0.03), rgba(0,0,0,0));
  }
  .backdrop--right {
    left: 880px; top: 280px; width: 200px; height: 200px;
    background: linear-gradient(180deg, rgba(0,0,0,0.03), rgba(0,0,0,0));
  }

  .brand {
    position: absolute; display: flex; align-items: center; gap: 8px;
    font-weight: 400; letter-spacing: 0.5px; text-transform: uppercase;
  }
  .brand__mark { width: 12px; height: 12px; border-radius: 50%; background: var(--green-dark); }
  .brand--header { left: 226px; top: 122px; font-size: 25px; color: var(--green-dark); }
  .brand--footer { left: 258px; top: 764px; font-size: 15px; color: #666; }
  .brand--footer .brand__mark { width: 8px; height: 8px; background: #666; }

  .divider { position: absolute; left: 856px; top: 0; width: 1px; height: 206px; background: var(--rule); }

  .contact {
    position: absolute; left: 875px; top: 99px;
    font-size: 8.6px; line-height: 13.6px; color: var(--ink-muted);
  }
  .contact__name { color: var(--green-dark); }
  .contact__email { color: var(--ink); }

  .hero {
    position: absolute; left: 217px; top: 206px; width: 640px; height: 240px;
    background: linear-gradient(100deg, #a9a39a 0%, #d8d6d0 30%, #c9c5bc 55%, #8d8a82 80%, #b4aea2 100%);
  }

  .nav { position: absolute; left: 857px; top: 206px; list-style: none; }
  .nav__item {
    position: relative; width: 128px; height: 22.4px; margin-bottom: 3.2px;
    font-size: 8.8px; line-height: 22.4px; padding-left: 19px; color: var(--ink);
  }
  .nav__item svg { position: absolute; left: 0; top: 0; }
  .nav__item span { position: relative; }
  .nav__item--active { color: #fff; }

  .tagline {
    position: absolute; left: 217px; top: 446px; width: 257px; height: 57px;
    background: var(--green-dark); color: #fff;
    font-weight: 700; font-size: 12.8px; text-align: center; line-height: 57px;
  }
  .panel-news { position: absolute; left: 217px; top: 503px; width: 257px; height: 221px; background: var(--panel-left); }
  .panel-main { position: absolute; left: 474px; top: 446px; width: 509px; height: 278px; background: var(--panel-right); }

  .heading { position: absolute; font-size: 10px; font-weight: 700; color: var(--ink); }
  .heading .accent-green { color: var(--green-text); }
  .heading .accent-orange { color: var(--orange); }

  .copy {
    position: absolute; font-size: 8.2px; line-height: 13.6px; color: var(--ink-soft);
    text-align: justify;
  }
  .copy p + p { margin-top: 13.6px; }

  .news { position: absolute; left: 246px; width: 197px; }
  .news__date { font-size: 8px; color: var(--green-dark); line-height: 13.6px; }
  .news__body { font-size: 8.2px; line-height: 13.6px; color: var(--ink-soft); text-align: justify; }

  .footer-copy { position: absolute; left: 505px; top: 766px; font-size: 8.2px; color: var(--ink); }
  .footer-copy .brand-link { color: var(--green-dark); }
  .footer-links { position: absolute; right: 248px; top: 766px; font-size: 8.2px; color: var(--ink-muted); }
  .footer-links .sep { margin: 0 6px; }
</style>
</head>
<body>
<div class="canvas">
  <div class="backdrop" role="img" aria-label="Faint handwritten physics equations in the background"></div>
  <div class="backdrop backdrop--lower" role="img" aria-label="Faint molecule diagram and printed science text in the background"></div>
  <div class="backdrop backdrop--right" role="img" aria-label="Faint printed science text in the background"></div>

  <div class="brand brand--header"><span class="brand__mark"></span>Harborline Talent</div>

  <div class="divider"></div>

  <address class="contact" style="font-style:normal">
    <div class="contact__name">Harborline Talent, Inc.</div>
    <div>118 Larkfield Avenue</div>
    <div>Marlow, MD 21900</div>
    <div>Fax: (410) 555-0187</div>
    <div class="contact__email">Email Us</div>
  </address>

  <div class="hero" role="img" aria-label="Laboratory bench with glass flasks and labelled sample bottles"></div>

  <ul class="nav">
    <li class="nav__item nav__item--active">
      <svg width="128" height="23" viewBox="0 0 128 23"><polygon points="0,0 115,0 127,11.2 115,22.4 0,22.4" fill="#0d3a1c"/></svg>
      <span>Home</span></li>
    <li class="nav__item"><svg width="128" height="23" viewBox="0 0 128 23"><polygon points="0,0 115,0 127,11.2 115,22.4 0,22.4" fill="#e4e4e4"/></svg><span>About us</span></li>
    <li class="nav__item"><svg width="128" height="23" viewBox="0 0 128 23"><polygon points="0,0 115,0 127,11.2 115,22.4 0,22.4" fill="#e4e4e4"/></svg><span>Expertise</span></li>
    <li class="nav__item"><svg width="128" height="23" viewBox="0 0 128 23"><polygon points="0,0 115,0 127,11.2 115,22.4 0,22.4" fill="#e4e4e4"/></svg><span>Employer Services</span></li>
    <li class="nav__item"><svg width="128" height="23" viewBox="0 0 128 23"><polygon points="0,0 115,0 127,11.2 115,22.4 0,22.4" fill="#e4e4e4"/></svg><span>Candidate Services</span></li>
    <li class="nav__item"><svg width="128" height="23" viewBox="0 0 128 23"><polygon points="0,0 115,0 127,11.2 115,22.4 0,22.4" fill="#e4e4e4"/></svg><span>Job Center</span></li>
    <li class="nav__item"><svg width="128" height="23" viewBox="0 0 128 23"><polygon points="0,0 115,0 127,11.2 115,22.4 0,22.4" fill="#e4e4e4"/></svg><span>Contact us</span></li>
  </ul>

  <div class="tagline">The Science of Recruiting</div>
  <div class="panel-news"></div>
  <div class="panel-main"></div>

  <h2 class="heading" style="left:246px; top:535px;">Last news</h2>
  <div class="news" style="top:566px;">
    <div class="news__date">March 20, 2010</div>
    <div class="news__body">Nulla porta et, accumsan nunc. Fusce vitae metus. Nullam laoreet, purus fringilla eget, vestibulum vehicula. Integer neque vel massa in.</div>
  </div>
  <div class="news" style="top:638px;">
    <div class="news__date">March 19, 2010</div>
    <div class="news__body">Integer sollicitudin eget, cursus vitae, arcu. Nulla ut urna. Nam pellentesque facilisis. Nulla ante. Maecenas mi at ligula. Cras tincidunt.</div>
  </div>

  <h2 class="heading" style="left:504px; top:480px;">Welcome to <span class="accent-green">Harborline</span> <span class="accent-orange">Talent</span></h2>
  <div class="copy" style="left:505px; top:511px; width:192px;">
    <p>Employees are every company's key to success. Harborline Talent is a recruiting and search firm distinctly focused on those industries we know best. We have placed employees at all levels throughout the United States.</p>
    <p>Our continued success and growth are a result of a consistent high level of service with unparalleled commitment to quality and integrity. We are a partner with our clients who rely on our network of candidates within the industry to help them achieve the next level of excellence.</p>
  </div>

  <h2 class="heading" style="left:758px; top:480px;">Our Approach</h2>
  <div class="copy" style="left:759px; top:511px; width:192px;">
    <p>Sed vitae est eu arcu id mi libero, id turpis sed ante. Curabitur ut justo a nunc sem, eleifend ac, porta eu, purus. Aenean non enim urna, placerat porttitor. Nulla ac erat. Pellentesque scelerisque a, fermentum odio. Suspendisse lectus semper id.</p>
    <p>Quisque adipiscing elit. Vestibulum non felis. Aenean id ipsum. Duis commodo est sem, rutrum consectetuer adipiscing elit. Mauris magna ipsum ac ornare a, adipiscing sed, ultrices posuere vitae, cursus consequat, metus nunc, nonummy turpis.</p>
  </div>

  <div class="brand brand--footer"><span class="brand__mark"></span>Harborline Talent</div>
  <div class="footer-copy">Copyright 2010 © <span class="brand-link">HarborlineTalent</span>  All rights reserved.</div>
  <div class="footer-links">Site map<span class="sep">/</span>Privacy policy</div>
</div>
</body>
</html>
```